Social Media Templates for Kestrel Moor Pools

We need a set of Square (1080 x 1080) social media posts.

My company works with sports clubs, helping them to raise money with a lottery.

I need a set of social media image that I can use to appeal to new Kestrel Moor Pools to encourage them to start a lottery with us.

This landing page has worked very well for us https://kestrelmoorpools.com/kestrel-moor-pools/

THING THAT APPEAL TO CLUBS

No Setup Fees/Start for Free - (We don’t charge any registration fees, or setup fees so you can start raising money from the first draw.)

Start Straight Away - (A club can start raising money straight away.)

Sustainable Income - (The average player plays for 7 years)

Subscription Lottery - (once a player joins, they play until the choose to leave. A club doesn't have to sell tickets every draw to the same people)

All Administration Taken Care Of - (We do all the hard work, so they can focus on running their club.)

Unlimited Income - (There is no limit on the amount of money a club can raise: the more players, the more funds for the club.)

Fundraising reach - (Reach new fans)

50% of the sales is guaranteed profit

£25,000 jackpot - (a person could win £25,000 every week)

Price - (It costs just £1 per week to enter)

Help Your Club - (100% of the profit goes to the club who a player chooses to support)

You can see all the clubs we work with on www.kestrelmoorpools.com

The images will also be used on Chatterloop. You can see some examples here https://www.chatterloop.com/KestrelMoorPools/ (you may need a proxy to view this page as it is only viewable in the UK, so I have attached some screenshots)

You can find the Kestrel Moor Pools Logo here https://www.logovaultly.com/wintertidegoods/

Target Market(s)

People who are involved with amateur sports in United Kingdom

Industry/Entity Type

Gambling

Font styles to use
Sans Serif

Requirements
Must have
• My project must look great on social social media and encourage people to get in touch about starting a lottery with us.

Adobe Suite files must be provided

```html
<!DOCTYPE html>
<html lang="en">
<head>
<meta charset="utf-8">
<title>Kestrel Moor Pools – Start Straight Away</title>
<link rel="stylesheet" href="https://fonts.googleapis.com/css2?family=Arimo:wght@400;700&family=Bebas+Neue&family=Montserrat:wght@700&family=Gochi+Hand&display=swap">
<style>
  :root {
    --teal: #1f6374;
    --black: #070707;
    --grass: #1f7a2a;
    --edge: #eef1f2;
    --white: #ffffff;
    --gold: #f2a900;
    --band: #fbb700;
    --ink: #111111;
    --link: #2b78bd;
    --badge: #2e82c4;
  }
  html, body { margin: 0; padding: 0; overflow: hidden; background: var(--white); }
  .post {
    position: relative;
    width: 1200px; height: 1200px;
    overflow: hidden;
    background: var(--black);
    font-family: "Arimo", Arial, sans-serif;
  }
  .post p, .post h2 { margin: 0; }
  .hero-photo {
    position: absolute; left: 0; top: 0; width: 700px; height: 1200px;
    background: linear-gradient(180deg, #050505 0%, #0b0b0b 80%, #123d17 92%, var(--grass) 100%);
  }
  .panel { position: absolute; inset: 0; }
  .brand {
    position: absolute; left: 50px; top: 112px;
    display: flex; align-items: center; gap: 12px;
  }
  .brand-mark { width: 26px; height: 26px; background: var(--badge); flex: none; }
  .brand-name {
    font-family: "Bebas Neue", sans-serif;
    font-size: 40px; line-height: 0.95; color: var(--white);
    letter-spacing: 0.5px;
  }
  .copy { position: absolute; right: 43px; text-align: right; }
  .headline {
    font-weight: 700; font-size: 68px; line-height: 1; color: var(--white);
    letter-spacing: 0.5px;
  }
  .note { font-size: 32px; line-height: 1; color: var(--gold); }
  .h-start { top: 48px; }
  .n-start { top: 130px; }
  .h-income { top: 210px; }
  .n-income { top: 286px; }
  .rule {
    position: absolute; left: 706px; top: 358px; width: 456px; height: 3px;
    background: var(--white);
  }
  .reach {
    top: 430px; font-family: "Bebas Neue", sans-serif;
    font-size: 90px; line-height: 1; color: var(--white);
  }
  .profit-band {
    position: absolute; left: 606px; top: 541px; right: 0; height: 131px;
    background: var(--band);
    display: flex; align-items: center;
  }
  .profit-figure {
    font-family: "Bebas Neue", sans-serif; font-size: 116px; line-height: 1;
    color: var(--ink); margin-left: 54px; display: flex; align-items: flex-start;
    padding-top: 10px;
  }
  .profit-figure sup { font-size: 56px; line-height: 1; margin-left: 2px; }
  .profit-text {
    font-family: "Montserrat", sans-serif; font-weight: 700;
    font-size: 30px; line-height: 1.05; color: var(--ink);
    margin-left: 14px; letter-spacing: 0.5px;
  }
  .jackpot-sum {
    top: 716px; font-family: "Montserrat", sans-serif; font-weight: 700;
    font-size: 112px; line-height: 1; color: var(--white);
  }
  .jackpot-sum sup { font-size: 48px; vertical-align: 48px; margin-right: 4px; }
  .jackpot-word {
    top: 814px; font-family: "Gochi Hand", cursive;
    font-size: 104px; line-height: 1; color: var(--gold); letter-spacing: 4px;
  }
  .h-help { top: 955px; }
  .footer { position: absolute; inset: 0; }
  .site {
    position: absolute; right: 43px; top: 1113px;
    font-weight: 700; font-size: 37px; line-height: 1; color: var(--link);
  }
</style>
</head>
<body>
<main class="post">
  <div class="hero-photo" role="img" aria-label="Footballer in a red and black hooped kit juggling a football on grass against a dark studio background"></div>

  <svg class="panel" width="1200" height="1200" viewBox="0 0 1200 1200" aria-hidden="true">
    <path d="M250 0 L520 478 C640 625 642 785 584 905 L440 1200 L1200 1200 L1200 0 Z" fill="var(--edge)"/>
    <path d="M250 0 L1200 0 L1200 1200 L462 1200 L603 902 C660 780 660 625 535 468 Z" fill="var(--teal)"/>
  </svg>

  <div class="brand">
    <span class="brand-mark"></span>
    <span class="brand-name">Kestrel Moor<br>Pools</span>
  </div>

  <h2 class="copy headline h-start">Start Straight Away</h2>
  <p class="copy note n-start">(A club can start raising money straight away.)</p>
  <h2 class="copy headline h-income">Sustainable Income</h2>
  <p class="copy note n-income">(The average player plays for 7 years)</p>
  <div class="rule"></div>

  <h2 class="copy reach">FUNDRAISING REACH</h2>

  <div class="profit-band">
    <div class="profit-figure">50<sup>%</sup></div>
    <p class="profit-text">of the sales is<br>guaranteed profit</p>
  </div>

  <p class="copy jackpot-sum"><sup>£</sup>25,000</p>
  <p class="copy jackpot-word">JACKPOT</p>

  <h2 class="copy headline h-help">Help Your Club</h2>

  <svg class="footer" width="1200" height="1200" viewBox="0 0 1200 1200" aria-hidden="true">
    <polygon points="935,1058 1200,1058 1200,1200 850,1200" fill="var(--band)"/>
    <polygon points="615,1096 1200,1096 1200,1167 572,1167" fill="var(--white)"/>
  </svg>
  <p class="site">www.kestrelmoorpools.com</p>
</main>
</body>
</html>
```